Investment fund website overhaul for modern aesthetic (example sites in description)

I would like to request an overhaul of our current website (www.silverbrookmeridianholdings.com), which craftly.net builders initially designed. The goal is to update the site's look and functionality while maintaining most of the existing page structure. Specifically, I'd like to implement the following changes:

Visual Redesign:
Please redesign the site to more closely resemble the style and aesthetic of the following three websites:
https://www.velmora.com/
https://www.tzq.com/
https://harborlynpartners.com/

New Portfolio, Meet the team, News & Insights:
Add a new "Portfolio" page to showcase our acquired businesses and properties. As we currently don't have any acquisitions, please include a "Coming Soon" message or placeholder content that explains our acquisition strategy and future plans.

Client Portal (a log in function):
Implement a secure client portal with the following features:
User authentication (username and password)
Ability for us to assign login credentials to investors
A personalized dashboard for each investor, displaying:
Their investments (API to come in the next several months)
Relevant legal documents
Personal information
Payment transfer (ACH/Wire/crypto)

Existing Pages:
Maintain the current site structure and content for existing pages but update their design to match the new aesthetic from those 3 websites.
Potentially change the names and additional pages (Who we are, What we do, Meet the Team, Our portfolio, News & Insights and then a separate client portal tab that sends them to a login in screen)

Please provide an estimate for these changes and a proposed timeline for completion. If you have any questions or need further clarification, please don't hesitate to ask.

Target Market(s)

Investors

Industry/Entity Type

AI, blockchain, digital assets, finance, and banking

Coding

Coded - Design and coding required

Number of Pages Required

5+ page

Colors

Designer to choose colors to be used in the design.

Requirements
Must have
• Pages: Who we are (landing/home page); What we do (mission page; Meet the team (coming soon); and Portfolio (Content coming soon)
Nice to have
• Client portal would be nice to have, but a simple but with the option and login credential page is fine for the time being.

```html
<!DOCTYPE html>
<html lang="en">
<head>
<meta charset="utf-8">
<title>Silverbrook Meridian Holdings – Home Concepts</title>
<link href="https://fonts.googleapis.com/css2?family=Noto+Serif:wght@400;500&family=Roboto:wght@400;500;700&display=swap" rel="stylesheet">
<style>
:root{
  --canvas:#f2f2f2;
  --white:#ffffff;
  --cream:#fbf9f3;
  --gold:#c9962e;
  --gold-light:#f6bb52;
  --gold-dark:#b3842a;
  --ink:#1c1c1c;
  --text:#4a4a4a;
  --line:#dcdcdc;
  --navy:#0c0b33;
  --serif:"Noto Serif",Georgia,serif;
  --sans:"Roboto",Arial,sans-serif;
}
*{box-sizing:border-box;margin:0;padding:0}
html,body{width:1200px;height:2548px;overflow:hidden}
body{background:var(--canvas);position:relative;font-family:var(--sans);color:var(--ink)}
.page{position:absolute;top:72px;width:503px;background:var(--white);box-shadow:0 0 6px rgba(0,0,0,.06);display:flex;flex-direction:column}
.page--a{left:67px}
.page--b{left:630px}
section,header,footer{position:relative;width:100%;flex:none}
.abs{position:absolute}

/* header */
.site-header{height:50px;display:flex;align-items:center;padding:0 47px}
.brand{display:flex;align-items:center;gap:5px}
.brand__mark{width:9px;height:9px;border-radius:50%;background:var(--gold)}
.brand__name{font-family:var(--serif);font-size:6.4px;line-height:1.05;color:#3a3a3a;letter-spacing:.2px;text-transform:uppercase}
.nav{display:flex;gap:11px;margin-left:28px;font-size:5px;color:#333}
.nav a{color:inherit;text-decoration:none}
.nav .is-active{color:var(--gold);text-decoration:underline}
.login{margin-left:auto;display:flex;align-items:center;gap:5px;font-size:5px;font-weight:700}
.login__icon{width:12px;height:12px;background:var(--gold)}

/* hero */
.hero{height:251px;overflow:hidden}
.hero--a{background:linear-gradient(180deg,#5d6468 0%,#8a7552 35%,#7a5a34 70%,#5a3f24 100%)}
.hero--b{background:radial-gradient(circle at 65% 50%,#c06a2a 0%,#3a3230 40%,#12222a 75%)}
.hero__title{font-family:var(--serif);color:var(--white);font-weight:400;text-transform:uppercase}
.hero--a .hero__title{left:0;right:0;top:97px;text-align:center;font-size:16.5px;line-height:22px}
.hero--b .hero__title{left:47px;top:69px;font-size:15px;line-height:21px}
.play{width:30px;height:30px;border-radius:50%;border:1px solid rgba(255,255,255,.8);display:flex;align-items:center;justify-content:center}
.play span{width:20px;height:20px;border-radius:50%;background:#fff;display:flex;align-items:center;justify-content:center}
.hero--a .play{left:237px;top:51px}
.hero--b .play{left:322px;top:112px}
.btn{display:inline-block;font-size:4.8px;font-weight:500;letter-spacing:.3px;padding:6px 9px;text-transform:uppercase;border:1px solid var(--gold);color:var(--ink);background:transparent}
.btn--solid{background:var(--gold);color:#fff;border-color:var(--gold)}
.btn--grad{background:linear-gradient(90deg,var(--gold-dark),var(--gold-light));color:#fff;border:none}
.btn--light{color:#fff;border-color:#fff}
.hero--a .btn{left:226px;top:146px}
.hero--b .btn{left:47px;top:163px}
.dots{left:232px;bottom:10px;display:flex;gap:4px}
.dots i{width:8px;height:1px;background:rgba(255,255,255,.5)}
.dots i.on{background:#fff}

/* profile */
.profile{height:274px;background:var(--cream);text-align:center}
.profile__icon{left:243px;top:34px;width:18px;height:18px;border-radius:50%;background:var(--gold)}
.eyebrow{font-size:5px;color:var(--gold-light);letter-spacing:.3px;text-transform:uppercase}
.profile .eyebrow{left:0;right:0;top:63px}
.section-title{font-family:var(--serif);font-weight:400;text-transform:uppercase;color:var(--ink)}
.profile .section-title{left:0;right:0;top:73px;font-size:13px}
.profile__lead{left:70px;right:70px;top:97px;font-size:6px;line-height:11px;color:#333}
.card{width:78px;height:62px;background:#fff;border:1px solid var(--line);padding:27px 4px 0;text-align:center}
.card__icon{position:absolute;left:25px;top:-13px;width:27px;height:27px;border-radius:50%;background:radial-gradient(circle,var(--gold-light),var(--gold-dark));border:2px solid #fff;box-shadow:0 0 0 1px #e8d6ad}
.card h4{font-size:5.6px;font-weight:500;text-transform:uppercase;line-height:8px}
.card p{font-size:4.2px;color:#555;line-height:6px;margin-top:4px}

/* about */
.about{height:211px}
.about .section-title{left:47px;top:40px;font-size:16px;line-height:22px}
.about .btn{left:47px;top:117px}
.about__body{left:232px;top:42px;width:229px;font-size:5.6px;line-height:10.8px;color:#444;text-align:justify}
.about__body p+p{margin-top:6px}

/* band */
.band{height:190px;background:linear-gradient(90deg,var(--gold-dark),var(--gold-light))}
.band__card{top:40px;width:91px;height:117px;background:#fff;padding:18px 8px}
.band__card i{display:block;width:22px;height:20px;background:linear-gradient(135deg,var(--gold-dark),var(--gold-light));margin-bottom:10px}
.band__card h4{font-size:6px;font-weight:700;line-height:12px;text-transform:uppercase}
.band__title{left:253px;top:37px;font-family:var(--serif);font-weight:400;color:#fff;font-size:14.5px;line-height:19.5px;text-transform:uppercase}
.band__text{left:253px;top:103px;width:204px;font-size:5.5px;line-height:10.8px;color:rgba(255,255,255,.85);text-align:justify}

/* verticals */
.vertical{height:260px}
.vertical--last{height:276px}
.vertical .divider{left:47px;right:47px;bottom:0;height:1px;background:var(--line)}
.vertical--last .divider{display:none}
.vertical__text{width:194px}
.vertical__text h3{font-family:var(--serif);font-weight:400;font-size:14px;line-height:20px;text-transform:uppercase}
.vertical__text p{font-size:5.5px;line-height:10.8px;color:#444;text-align:justify;margin:9px 0 12px}
.frame{width:181px;height:180px;border:1px solid var(--line)}
.photo{width:180px;height:180px}
.photo--cyber{background:radial-gradient(circle at 50% 45%,#6aa6c7 0%,#1f4a6e 40%,#0d1f38 80%)}
.photo--build{background:linear-gradient(180deg,#7f9fb5 0%,#c9a378 45%,#e89a3e 70%,#3a2a1e 100%)}
.photo--estate{background:linear-gradient(90deg,#8e979c,#e4e7e8 50%,#9aa2a7)}
.photo--digital{background:radial-gradient(circle at 50% 45%,#d7a15a 0%,#3c5d85 35%,#172c4c 80%)}

/* cta */
.cta{height:217px;background:linear-gradient(120deg,#2f5f86 0%,#1f4467 45%,#6a9cc4 70%,#13253d 100%)}
.cta__box{left:47px;top:32px;width:206px;height:185px;background:rgba(255,255,255,.22);padding:28px 20px}
.cta__box h2{font-family:var(--serif);font-weight:400;color:#fff;font-size:14.5px;line-height:20px;text-transform:uppercase}
.cta__box p{font-size:5.5px;line-height:10.8px;color:#f0f4f8;margin:10px 0 12px}

/* footer */
.site-footer{height:154px;background:var(--navy);color:#fff}
.site-footer .brand{position:absolute;left:47px;top:72px}
.site-footer .brand__name{color:#e9e2cf;font-size:6.6px}
.site-footer .brand__mark{width:11px;height:11px}
.fcol h5{font-size:6px;font-weight:700;text-transform:uppercase;margin-bottom:9px}
.fcol li{list-style:none;font-size:4.8px;line-height:13.3px}
.fcol li::before{content:"›";color:var(--gold-light);margin-right:5px}
.newsletter{width:126px;height:19px;background:#fff;color:#333;font-size:4.8px;display:flex;align-items:center;justify-content:space-between;padding:0 7px}
.newsletter i{width:6px;height:6px;border-top:1px solid var(--gold);border-right:1px solid var(--gold);transform:rotate(45deg)}
.footer__rule{left:47px;right:47px;top:128px;height:1px;background:rgba(255,255,255,.15)}
.copyright{left:0;right:0;top:138px;text-align:center;font-size:4.8px;color:#d8d8e2}
</style>
</head>
<body>

<!-- Concept A -->
<div class="page page--a">
  <header class="site-header">
    <div class="brand"><span class="brand__mark"></span><span class="brand__name">Silverbrook Meridian<br>Holdings, LLC</span></div>
    <nav class="nav"><a class="is-active">Home</a><a>Who We Are</a><a>What We Do</a><a>Meet The Team</a><a>Our Portfolio</a><a>News &amp; Insights</a></nav>
    <div class="login"><span class="login__icon"></span>LOGIN</div>
  </header>

  <section class="hero hero--a" role="img" aria-label="Photo of horses grazing in a mountain valley">
    <div class="abs play"><span><svg width="6" height="7" viewBox="0 0 6 7"><path d="M0 0L6 3.5L0 7Z" fill="#333"/></svg></span></div>
    <h1 class="abs hero__title">Where Technology<br>Meets Strategic Investment</h1>
    <span class="abs btn btn--solid">Learn More</span>
    <div class="abs dots"><i></i><i class="on"></i><i></i><i></i></div>
  </section>

  <section class="profile">
    <div class="abs profile__icon"></div>
    <div class="abs eyebrow">Focus Firm Synopsis</div>
    <h2 class="abs section-title">Target Company Profile</h2>
    <p class="abs profile__lead">SMH seeks companies with stable revenue streams and strong growth potential through strategic technological advancements and operational efficiencies.</p>
    <div class="abs card" style="left:7px;top:148px"><span class="card__icon"></span><h4>Revenue</h4><p>$5 million - $50 million annually</p></div>
    <div class="abs card" style="left:90px;top:178px"><span class="card__icon"></span><h4>EBITDA</h4><p>$1 million - $10 million</p></div>
    <div class="abs card" style="left:173px;top:148px"><span class="card__icon"></span><h4>Employee Size</h4><p>20 - 200 employees</p></div>
    <div class="abs card" style="left:257px;top:178px"><span class="card__icon"></span><h4>Industry<br>Focus</h4><p>Cybersecurity, construction, trade services, specialized commercial real estate</p></div>
    <div class="abs card" style="left:340px;top:148px"><span class="card__icon"></span><h4>Growth<br>Potential</h4><p>Stable with opportunities for technological enhancement</p></div>
    <div class="abs card" style="left:424px;top:178px"><span class="card__icon"></span><h4>Technology<br>Integration</h4><p>Companies that can benefit from AI, blockchain, and Bitcoin adoption.</p></div>
  </section>

  <section class="about">
    <h2 class="abs section-title">Silverbrook<br>Meridian<br>Holdings (SMH)</h2>
    <span class="abs btn">Learn More</span>
    <div class="abs about__body">
      <p>At Silverbrook Meridian Holdings, LLC, we are poised to revolutionize industries by leveraging cutting-edge AI and blockchain technologies. With a bold vision and resilience, we are ready to drive transformative growth and capture unparalleled opportunities in the market.</p>
      <p>We are a forward-thinking search fund dedicated to driving economic growth by strategically acquiring small to medium-sized businesses in high-potential verticals: Cybersecurity, Construction and Trade Services, and Specialized Commercial Real Estate.</p>
      <p>We target industries positioned for significant growth, address critical market needs with innovative solutions, and generate sustainable, long-term returns by leveraging our expertise in scaling and optimizing business operations.</p>
    </div>
  </section>

  <section class="band">
    <div class="abs band__card" style="left:47px"><i></i><h4>Targeting high-potential industries for growth</h4></div>
    <div class="abs band__card" style="left:151px"><i></i><h4>Scaling and optimizing business operations for long-term returns</h4></div>
    <h2 class="abs band__title">Driving Economic<br>Growth Through<br>Strategic Acquisitions</h2>
    <p class="abs band__text">At Silverbrook Meridian Holdings, LLC, we are poised to revolutionize industries by leveraging cutting-edge AI and blockchain technologies. With a bold vision and resilience, we are ready to drive transformative growth and capture unparalleled opportunities in the market.</p>
  </section>

  <section class="vertical">
    <div class="abs vertical__text" style="left:47px;top:60px"><h3>Cybersecurity</h3><p>Americans and their small to medium-sized businesses are highly vulnerable to increasing cyberattacks, making cybersecurity safeguards essential to daily operations. SMH intends to acquire and grow a leading cybersecurity firm, integrating advanced technologies like blockchain and AI to provide military-grade security solutions. By enhancing protection and operational efficiency, these businesses will offer stable returns, safeguarding investments in both good and bad times.</p><span class="btn">Learn More</span></div>
    <div class="abs frame" style="left:279px;top:41px"></div>
    <div class="abs photo photo--cyber" style="left:269px;top:51px" role="img" aria-label="Businessman holding a glowing digital security shield"></div>
    <div class="abs divider"></div>
  </section>

  <section class="vertical">
    <div class="abs frame" style="left:47px;top:38px"></div>
    <div class="abs photo photo--build" style="left:58px;top:49px" role="img" aria-label="Construction workers silhouetted on steel framing at sunset"></div>
    <div class="abs vertical__text" style="left:264px;top:60px"><h3>Construction and<br>Trade Services</h3><p>Essential trade services like electrical, plumbing, and HVAC are often inefficient and can greatly benefit from technological advancements. SMH acquires businesses in these sectors and integrates AI and innovative technologies to improve efficiency and scalability. These upgrades ensure these companies remain vital and profitable, providing a strong foundation for returns regardless of economic conditions.</p><span class="btn btn--grad">Learn More</span></div>
    <div class="abs divider"></div>
  </section>

  <section class="vertical">
    <div class="abs vertical__text" style="left:47px;top:50px"><h3>Specialized<br>Commercial Real<br>Estate</h3><p>The growing demand for both physical and data storage solutions presents a significant challenge. SMH targets high-potential storage and warehouse facilities, utilizing innovations like vertical warehousing and IoT technology to optimize space and operations. These strategic enhancements address urban land scarcity and ensure consistent demand, making these investments resilient and profitable in varying economic climates.</p><span class="btn">Learn More</span></div>
    <div class="abs frame" style="left:279px;top:37px"></div>
    <div class="abs photo photo--estate" style="left:269px;top:47px" role="img" aria-label="Two professionals walking through a glass office corridor"></div>
    <div class="abs divider"></div>
  </section>

  <section class="vertical vertical--last">
    <div class="abs frame" style="left:47px;top:38px"></div>
    <div class="abs photo photo--digital" style="left:58px;top:49px" role="img" aria-label="Hand holding a glowing digital coin over a city skyline"></div>
    <div class="abs vertical__text" style="left:264px;top:62px"><h3>Digital Assets</h3><p>Treasury assets should actively work for the company rather than sit idle. SMH leverages Bitcoin as a dynamic treasury asset, using its potential for collateralization to facilitate acquisitions, lending operations, and custodial services within our cybersecurity firm. By adopting Bitcoin and investing in cutting-edge blockchain technologies, we position ourselves to benefit from the accelerating adoption of AI and blockchain.</p><span class="btn">Learn More</span></div>
  </section>

  <section class="cta" role="img" aria-label="Hand touching a rising arrow growth chart on blue background">
    <div class="abs cta__box"><h2>Invest in Your<br>Future Today</h2><p>Discover high-potential investment opportunities in the Cybersecurity, Trade &amp; Construction Services, and Specialized CRE industries.</p><span class="btn btn--light">Contact Us</span></div>
  </section>

  <footer class="site-footer">
    <div class="brand"><span class="brand__mark"></span><span class="brand__name">Silverbrook Meridian<br>Holdings, LLC</span></div>
    <div class="abs fcol" style="left:189px;top:26px"><h5>Navigation</h5><ul><li>Home</li><li>Who We Are</li><li>What We Do</li><li>Meet The Team</li><li>Our Portfolio</li><li>News &amp; Insights</li></ul></div>
    <div class="abs fcol" style="left:266px;top:26px"><h5>Quick Links</h5><ul><li>Privacy Policy</li><li>Terms Of Use</li><li>Legal Support</li><li>Disclaimer</li></ul></div>
    <div class="abs fcol" style="left:330px;top:26px"><h5>Sign Up To Our Newsletter</h5><div class="newsletter">Email Address<i></i></div></div>
    <div class="abs footer__rule"></div>
    <div class="abs copyright">© 2024. All Rights Reserved.</div>
  </footer>
</div>

<!-- Concept B -->
<div class="page page--b">
  <header class="site-header">
    <div class="brand"><span class="brand__mark"></span><span class="brand__name">Silverbrook Meridian<br>Holdings, LLC</span></div>
    <nav class="nav"><a class="is-active">Home</a><a>Who We Are</a><a>What We Do</a><a>Meet The Team</a><a>Our Portfolio</a><a>News &amp; Insights</a></nav>
    <div class="login"><span class="login__icon"></span>LOGIN</div>
  </header>

  <section class="hero hero--b" role="img" aria-label="Hand touching a glowing digital globe over orange market charts">
    <h1 class="abs hero__title">Where<br>Technology<br>Meets Strategic<br>Investment</h1>
    <span class="abs btn btn--light">Learn More</span>
    <div class="abs play"><span><svg width="6" height="7" viewBox="0 0 6 7"><path d="M0 0L6 3.5L0 7Z" fill="#333"/></svg></span></div>
    <div class="abs dots"><i></i><i class="on"></i><i></i><i></i></div>
  </section>

  <section class="profile">
    <div class="abs profile__icon"></div>
    <div class="abs eyebrow">Focus Firm Synopsis</div>
    <h2 class="abs section-title">Target Company Profile</h2>
    <p class="abs profile__lead">SMH seeks companies with stable revenue streams and strong growth potential through strategic technological advancements and operational efficiencies.</p>
    <div class="abs card" style="left:7px;top:148px"><span class="card__icon"></span><h4>Revenue</h4><p>$5 million - $50 million annually</p></div>
    <div class="abs card" style="left:90px;top:178px"><span class="card__icon"></span><h4>EBITDA</h4><p>$1 million - $10 million</p></div>
    <div class="abs card" style="left:173px;top:148px"><span class="card__icon"></span><h4>Employee Size</h4><p>20 - 200 employees</p></div>
    <div class="abs card" style="left:257px;top:178px"><span class="card__icon"></span><h4>Industry<br>Focus</h4><p>Cybersecurity, construction, trade services, specialized commercial real estate</p></div>
    <div class="abs card" style="left:340px;top:148px"><span class="card__icon"></span><h4>Growth<br>Potential</h4><p>Stable with opportunities for technological enhancement</p></div>
    <div class="abs card" style="left:424px;top:178px"><span class="card__icon"></span><h4>Technology<br>Integration</h4><p>Companies that can benefit from AI, blockchain, and Bitcoin adoption.</p></div>
  </section>

  <section class="about">
    <h2 class="abs section-title">Silverbrook<br>Meridian<br>Holdings (SMH)</h2>
    <span class="abs btn">Learn More</span>
    <div class="abs about__body">
      <p>At Silverbrook Meridian Holdings, LLC, we are poised to revolutionize industries by leveraging cutting-edge AI and blockchain technologies. With a bold vision and resilience, we are ready to drive transformative growth and capture unparalleled opportunities in the market.</p>
      <p>We are a forward-thinking search fund dedicated to driving economic growth by strategically acquiring small to medium-sized businesses in high-potential verticals: Cybersecurity, Construction and Trade Services, and Specialized Commercial Real Estate.</p>
      <p>We target industries positioned for significant growth, address critical market needs with innovative solutions, and generate sustainable, long-term returns by leveraging our expertise in scaling and optimizing business operations.</p>
    </div>
  </section>

  <section class="band">
    <div class="abs band__card" style="left:47px"><i></i><h4>Targeting high-potential industries for growth</h4></div>
    <div class="abs band__card" style="left:151px"><i></i><h4>Scaling and optimizing business operations for long-term returns</h4></div>
    <h2 class="abs band__title">Driving Economic<br>Growth Through<br>Strategic Acquisitions</h2>
    <p class="abs band__text">At Silverbrook Meridian Holdings, LLC, we are poised to revolutionize industries by leveraging cutting-edge AI and blockchain technologies. With a bold vision and resilience, we are ready to drive transformative growth and capture unparalleled opportunities in the market.</p>
  </section>

  <section class="vertical">
    <div class="abs vertical__text" style="left:47px;top:60px"><h3>Cybersecurity</h3><p>Americans and their small to medium-sized businesses are highly vulnerable to increasing cyberattacks, making cybersecurity safeguards essential to daily operations. SMH intends to acquire and grow a leading cybersecurity firm, integrating advanced technologies like blockchain and AI to provide military-grade security solutions. By enhancing protection and operational efficiency, these businesses will offer stable returns, safeguarding investments in both good and bad times.</p><span class="btn">Learn More</span></div>
    <div class="abs frame" style="left:279px;top:41px"></div>
    <div class="abs photo photo--cyber" style="left:269px;top:51px" role="img" aria-label="Businessman holding a glowing digital security shield"></div>
    <div class="abs divider"></div>
  </section>

  <section class="vertical">
    <div class="abs frame" style="left:47px;top:38px"></div>
    <div class="abs photo photo--build" style="left:58px;top:49px" role="img" aria-label="Construction workers silhouetted on steel framing at sunset"></div>
    <div class="abs vertical__text" style="left:264px;top:60px"><h3>Construction and<br>Trade Services</h3><p>Essential trade services like electrical, plumbing, and HVAC are often inefficient and can greatly benefit from technological advancements. SMH acquires businesses in these sectors and integrates AI and innovative technologies to improve efficiency and scalability. These upgrades ensure these companies remain vital and profitable, providing a strong foundation for returns regardless of economic conditions.</p><span class="btn btn--grad">Learn More</span></div>
    <div class="abs divider"></div>
  </section>

  <section class="vertical">
    <div class="abs vertical__text" style="left:47px;top:50px"><h3>Specialized<br>Commercial Real<br>Estate</h3><p>The growing demand for both physical and data storage solutions presents a significant challenge. SMH targets high-potential storage and warehouse facilities, utilizing innovations like vertical warehousing and IoT technology to optimize space and operations. These strategic enhancements address urban land scarcity and ensure consistent demand, making these investments resilient and profitable in varying economic climates.</p><span class="btn">Learn More</span></div>
    <div class="abs frame" style="left:279px;top:37px"></div>
    <div class="abs photo photo--estate" style="left:269px;top:47px" role="img" aria-label="Two professionals walking through a glass office corridor"></div>
    <div class="abs divider"></div>
  </section>

  <section class="vertical vertical--last">
    <div class="abs frame" style="left:47px;top:38px"></div>
    <div class="abs photo photo--digital" style="left:58px;top:49px" role="img" aria-label="Hand holding a glowing digital coin over a city skyline"></div>
    <div class="abs vertical__text" style="left:264px;top:62px"><h3>Digital Assets</h3><p>Treasury assets should actively work for the company rather than sit idle. SMH leverages Bitcoin as a dynamic treasury asset, using its potential for collateralization to facilitate acquisitions, lending operations, and custodial services within our cybersecurity firm. By adopting Bitcoin and investing in cutting-edge blockchain technologies, we position ourselves to benefit from the accelerating adoption of AI and blockchain.</p><span class="btn">Learn More</span></div>
  </section>

  <section class="cta" role="img" aria-label="Hand touching a rising arrow growth chart on blue background">
    <div class="abs cta__box"><h2>Invest in Your<br>Future Today</h2><p>Discover high-potential investment opportunities in the Cybersecurity, Trade &amp; Construction Services, and Specialized CRE industries.</p><span class="btn btn--light">Contact Us</span></div>
  </section>

  <footer class="site-footer">
    <div class="brand"><span class="brand__mark"></span><span class="brand__name">Silverbrook Meridian<br>Holdings, LLC</span></div>
    <div class="abs fcol" style="left:189px;top:26px"><h5>Navigation</h5><ul><li>Home</li><li>Who We Are</li><li>What We Do</li><li>Meet The Team</li><li>Our Portfolio</li><li>News &amp; Insights</li></ul></div>
    <div class="abs fcol" style="left:266px;top:26px"><h5>Quick Links</h5><ul><li>Privacy Policy</li><li>Terms Of Use</li><li>Legal Support</li><li>Disclaimer</li></ul></div>
    <div class="abs fcol" style="left:330px;top:26px"><h5>Sign Up To Our Newsletter</h5><div class="newsletter">Email Address<i></i></div></div>
    <div class="abs footer__rule"></div>
    <div class="abs copyright">© 2024. All Rights Reserved.</div>
  </footer>
</div>

</body>
</html>
```